Plumbing website that stands out

Seo optimized, mobile friendly, easily editable word press Plumbing website with google reviews widget. And widget of revolving photos of completed work. Contact page and services page, about page. Will provide, “About” content. And photos Need all other content written.
Services include:
Water heater replacement
Tankless water heater installation
Kitchen and bath remodel
Drain cleaning and clog removal
Leak repair
Faucet repair and replacement

I will be adding services and photos of recent completed projects as time goes on.

```html
<!DOCTYPE html>
<html lang="en">
<head>
<meta charset="utf-8">
<title>Clearflow Plumbing – Website Design</title>
<link href="https://fonts.googleapis.com/css2?family=Cinzel:wght@500;600&family=Montserrat:wght@400;500;600;700&display=swap" rel="stylesheet">
<style>
:root{
  --navy:#2d5c9c;
  --navy-dark:#234a80;
  --sky:#5db6d2;
  --ink:#2b2b2b;
  --grey-text:#555b61;
  --grey-band:#616469;
  --soft-grey:#ececec;
  --board:#e8f2fa;
  --white:#ffffff;
  --star:#f5b301;
  --footer-dark:#1d252d;
}
*{box-sizing:border-box;margin:0;padding:0}
html,body{width:1200px;height:4038px;overflow:hidden}
body{position:relative;background:var(--white);font-family:'Montserrat',sans-serif;color:var(--ink)}
.abs{position:absolute}
.board-bg{position:absolute;left:0;top:873px;width:1200px;height:3165px;background:var(--board)}

/* brand wordmark */
.brand{position:absolute;left:0;width:1200px;text-align:center}
.brand-mark{display:block;width:46px;height:46px;margin:0 auto 18px;background:var(--navy)}
.brand-name{font-family:'Cinzel',serif;font-weight:600;font-size:34px;letter-spacing:6px;color:var(--navy)}
.brand--top{top:44px}
.brand--bottom{top:3712px}

.board-title{position:absolute;top:930px;font-weight:700;font-size:26px;color:#111;text-align:center}

/* ---------- shared website pieces ---------- */
.site{position:absolute;background:var(--white);overflow:hidden;box-shadow:0 4px 18px rgba(30,60,100,.12)}
.topbar{position:absolute;left:0;top:0;width:100%;height:19px;background:var(--navy);color:var(--white);font-size:6.5px;font-weight:500}
.topbar span{position:absolute;top:5px;display:flex;align-items:center;gap:4px}
.ico{width:8px;height:8px;fill:currentColor}
.nav{position:absolute;top:19px;left:0;width:100%;height:34px;background:var(--white)}
.nav a{position:absolute;top:13px;font-size:6.8px;font-weight:700;color:var(--ink);text-decoration:none}
.nav a.active{border-bottom:1.5px solid var(--navy);padding-bottom:6px}
.logo-tab{position:absolute;top:19px;width:122px;height:62px;filter:drop-shadow(0 2px 2px rgba(0,0,0,.08))}
.logo-word{position:absolute;font-family:'Cinzel',serif;font-weight:600;color:var(--navy);text-align:center;line-height:1.15;letter-spacing:1.5px}

.photo{position:absolute;border-radius:0}
.ph-kitchen{background:linear-gradient(100deg,#f3f5f6 0%,#dfe5ea 35%,#c7d0d6 55%,#e8ecee 72%,#aeb7be 100%)}
.ph-plumber{background:linear-gradient(135deg,#c9c9c6 0%,#8f9aa3 40%,#4e5f73 70%,#d9cdbb 100%)}
.ph-sink{background:linear-gradient(150deg,#e5e2dc 0%,#a8b3bd 45%,#2f4f8f 70%,#e8e6e1 100%)}
.ph-van{background:linear-gradient(160deg,#f4f4f4 0%,#e4e6e9 45%,#c6ccd3 75%,#e8e8e8 100%)}

.hero-box{position:absolute;background:rgba(255,255,255,.9)}
.hero-serif{font-family:'Cinzel',serif;font-weight:500;color:var(--ink)}
.hero-sans{font-weight:600;color:var(--ink)}
.hero-copy{font-weight:600;color:var(--ink)}
.btn{position:absolute;display:flex;align-items:center;justify-content:center;background:var(--navy);color:var(--white);font-weight:600;letter-spacing:.3px}
.btn--light{background:var(--white);color:var(--navy)}
.dots{position:absolute;height:11px;width:38px;border-radius:6px;background:rgba(255,255,255,.85);display:flex;align-items:center;justify-content:center;gap:4px}
.dots i{width:4px;height:4px;border-radius:50%;border:1px solid #9aa6b1}
.dots i.on{background:var(--navy);border-color:var(--navy)}

.frame{position:absolute;border:2px solid var(--navy);border-radius:14px;padding:5px;background:var(--white)}
.frame--white{border-color:var(--white);background:transparent}
.frame .photo{position:static;width:100%;height:100%;border-radius:10px}

.sec-title{font-weight:500;color:#3c3f44;letter-spacing:.3px}
.sec-title em{font-style:normal;color:var(--sky)}
.body-copy{color:var(--grey-text)}

.svc-list{position:absolute;list-style:none;color:var(--white);font-weight:500}
.svc-list li{display:flex;align-items:center}
.tick{fill:none;stroke:var(--white);stroke-width:1.6}

.review{position:absolute;background:var(--white);box-shadow:0 2px 10px rgba(0,0,0,.1)}
.review .g-dot{position:absolute;width:9px;height:9px;border-radius:50%;background:#d7dde3}
.stars{position:absolute;display:flex;gap:1px}
.stars svg{width:5px;height:5px;fill:var(--star)}
.review p{position:absolute;color:var(--grey-text)}
.review .who{position:absolute;font-family:'Cinzel',serif;font-weight:600;color:var(--ink)}
.quote{position:absolute;font-family:Georgia,serif;font-weight:700;color:var(--navy)}

.field{position:absolute;background:var(--white);border:1px solid #d5d8dc;color:#777;display:flex;align-items:center}

.foot-h{position:absolute;color:var(--white);font-weight:600;letter-spacing:.3px}
.foot-t{position:absolute;color:#dfe4ea}
.foot-t b{font-weight:600;color:var(--white)}
.pin{fill:var(--white)}
.hours{position:absolute;color:#dfe4ea;font-weight:500}
.hours div{display:flex}
.hours b{font-weight:700;color:var(--white)}
.social{position:absolute;display:flex;gap:5px}
.social i{border:1px solid var(--white);border-radius:50%}
</style>
</head>
<body>
<svg width="0" height="0" style="position:absolute">
  <defs>
    <symbol id="i-phone" viewBox="0 0 24 24"><path d="M6.6 10.8a15.1 15.1 0 0 0 6.6 6.6l2.2-2.2a1 1 0 0 1 1-.25 11.4 11.4 0 0 0 3.6.57 1 1 0 0 1 1 1V20a1 1 0 0 1-1 1A17 17 0 0 1 3 4a1 1 0 0 1 1-1h3.5a1 1 0 0 1 1 1c0 1.25.2 2.45.57 3.57a1 1 0 0 1-.25 1z"/></symbol>
    <symbol id="i-mail" viewBox="0 0 24 24"><path d="M2 5h20v14H2z M3.5 6.5 12 13l8.5-6.5" fill="none" stroke="currentColor" stroke-width="2"/></symbol>
    <symbol id="i-pin" viewBox="0 0 24 24"><path d="M12 2a7 7 0 0 0-7 7c0 5.3 7 13 7 13s7-7.7 7-13a7 7 0 0 0-7-7zm0 9.5A2.5 2.5 0 1 1 12 6.5a2.5 2.5 0 0 1 0 5z"/></symbol>
    <symbol id="i-star" viewBox="0 0 24 24"><path d="M12 2l3 6.9 7.5.7-5.7 5 1.7 7.4L12 18.3 5.5 22l1.7-7.4-5.7-5 7.5-.7z"/></symbol>
    <symbol id="i-tick" viewBox="0 0 16 16"><rect x="1.5" y="1.5" width="13" height="13" rx="2"/><path d="M4.5 8.3l2.4 2.4 5-5.4"/></symbol>
    <linearGradient id="g-house" x1="0" y1="0" x2="1" y2="1">
      <stop offset="0" stop-color="#4a77b0"/><stop offset=".5" stop-color="#3a67a3"/><stop offset="1" stop-color="#335d95"/>
    </linearGradient>
    <linearGradient id="g-city" x1="0" y1="0" x2="0" y2="1">
      <stop offset="0" stop-color="#34404b"/><stop offset=".55" stop-color="#232c35"/><stop offset="1" stop-color="#3a3328"/>
    </linearGradient>
    <symbol id="logo-tab" viewBox="0 0 122 62"><path d="M0 0h122v40L61 62 0 40z" fill="#fff"/></symbol>
  </defs>
</svg>

<!-- ================= top wordmark ================= -->
<div class="brand brand--top"><span class="brand-mark"></span><span class="brand-name">CLEARFLOW PLUMBING</span></div>

<!-- ================= hero showcase (flat) ================= -->
<section class="site" style="left:249px;top:262px;width:702px;height:440px">
  <div class="topbar">
    <span style="left:94px"><svg class="ico"><use href="#i-phone"/></svg>Call Us Today : 123-456-7890</span>
    <span style="left:485px"><svg class="ico"><use href="#i-mail"/></svg>info@clearflowplumbing.com</span>
  </div>
  <div class="photo ph-kitchen" style="left:0;top:53px;width:702px;height:387px" role="img" aria-label="Photo of a plumber shaking hands with a homeowner in a bright kitchen"></div>
  <nav class="nav"><a class="active" style="left:95px">HOME</a><a style="left:143px">ABOUT US</a><a style="left:494px">SERVICES</a><a style="left:553px">CONTACT US</a></nav>
  <svg class="logo-tab" style="left:290px"><use href="#logo-tab"/></svg>
  <div class="logo-word" style="left:290px;top:42px;width:122px;font-size:9px">CLEARFLOW<br>PLUMBING</div>
  <div class="hero-box" style="left:94px;top:116px;width:266px;height:176px">
    <div class="hero-serif abs" style="left:14px;top:14px;font-size:22px">CLEARFLOW</div>
    <div class="hero-sans abs" style="left:14px;top:40px;font-size:18.5px">PLUMBING SERVICES</div>
    <p class="hero-copy abs" style="left:14px;top:70px;width:240px;font-size:9.6px;line-height:15.5px">Lorem ipsum dolor sit amet, consectetur adipiscij incididunt ut laboreet dolore magna olighu atnim amet.</p>
    <div class="btn" style="left:14px;top:136px;width:88px;height:22px;font-size:7.5px">GET A QUOTE</div>
  </div>
  <div class="dots" style="left:332px;top:370px"><i></i><i class="on"></i><i></i></div>
  <svg class="abs" style="left:0;top:280px" width="702" height="160" viewBox="0 0 702 160"><polygon points="0,65 347,128 702,10 702,160 0,160" fill="#5db6d2"/><polygon points="0,98 347,160 702,38 702,160 0,160" fill="#fff"/></svg>
</section>

<div class="board-bg"></div>
<h2 class="board-title" style="left:83px;width:702px">Home Desktop Version</h2>
<h2 class="board-title" style="left:830px;width:277px">Mobile Version</h2>

<!-- ================= desktop page ================= -->
<section class="site" style="left:83px;top:993px;width:702px;height:2242px">
  <div class="topbar">
    <span style="left:94px"><svg class="ico"><use href="#i-phone"/></svg>Call Us Today : 123-456-7890</span>
    <span style="left:485px"><svg class="ico"><use href="#i-mail"/></svg>info@clearflowplumbing.com</span>
  </div>
  <div class="photo ph-kitchen" style="left:0;top:53px;width:702px;height:387px" role="img" aria-label="Photo of a plumber shaking hands with a homeowner in a bright kitchen"></div>
  <nav class="nav"><a class="active" style="left:95px">HOME</a><a style="left:143px">ABOUT US</a><a style="left:494px">SERVICES</a><a style="left:553px">CONTACT US</a></nav>
  <svg class="logo-tab" style="left:290px"><use href="#logo-tab"/></svg>
  <div class="logo-word" style="left:290px;top:42px;width:122px;font-size:9px">CLEARFLOW<br>PLUMBING</div>
  <div class="hero-box" style="left:94px;top:116px;width:266px;height:176px">
    <div class="hero-serif abs" style="left:14px;top:14px;font-size:22px">CLEARFLOW</div>
    <div class="hero-sans abs" style="left:14px;top:40px;font-size:18.5px">PLUMBING SERVICES</div>
    <p class="hero-copy abs" style="left:14px;top:70px;width:240px;font-size:9.6px;line-height:15.5px">Lorem ipsum dolor sit amet, consectetur adipiscij incididunt ut laboreet dolore magna olighu atnim amet.</p>
    <div class="btn" style="left:14px;top:136px;width:88px;height:22px;font-size:7.5px">GET A QUOTE</div>
  </div>
  <div class="dots" style="left:332px;top:370px"><i></i><i class="on"></i><i></i></div>
  <svg class="abs" style="left:0;top:280px" width="702" height="160" viewBox="0 0 702 160"><polygon points="0,65 347,128 702,10 702,160 0,160" fill="#5db6d2"/><polygon points="0,98 347,160 702,38 702,160 0,160" fill="#fff"/></svg>

  <!-- about -->
  <div class="frame" style="left:94px;top:508px;width:216px;height:178px"><div class="photo ph-plumber" role="img" aria-label="Photo of a plumber fitting a kitchen faucet"></div></div>
  <h3 class="sec-title abs" style="left:346px;top:498px;font-size:16px;line-height:20px">ABOUT<br>CLEARFLOW <em>PLUMBING</em></h3>
  <div class="body-copy abs" style="left:346px;top:545px;width:258px;font-size:6.4px;line-height:13.4px">
    <p>Lorem Ipsum is simply dummy text of the printing and typesettiustry. Lorem Ipsum has been the industry's standard dummy text ever since the 1500s, when an unknown printer took a galley of type andrambled it to make a type specimenk. Ithas survived not only five centuries.</p>
    <p style="margin-top:3px">remaining essentially unchanged. It was popularised in the 1960s with the release of Typeset sheets containing Lorem Ipsum passages, and more recently with desktop publishing software like Folio Layout including versions of Lorem Ipsum.</p>
  </div>
  <div class="btn" style="left:346px;top:670px;width:88px;height:22px;font-size:7.5px">CONTACT US</div>

  <!-- services -->
  <svg class="abs" style="left:0;top:740px" width="702" height="560" viewBox="0 0 702 560" role="img" aria-label="Suburban house photo under a blue overlay">
    <polygon points="0,132 347,12 702,122 702,160 0,160" fill="#616469"/>
    <polygon points="0,420 347,510 702,420 702,455 347,550 0,460" fill="#616469"/>
    <polygon points="0,140 347,45 702,128 702,425 347,512 0,425" fill="url(#g-house)"/>
  </svg>
  <h3 class="abs" style="left:0;top:866px;width:702px;text-align:center;color:#fff;font-weight:500;font-size:15px">OUR SERVICES</h3>
  <p class="abs" style="left:145px;top:890px;width:412px;text-align:center;color:#e6eef8;font-size:7px;line-height:12px">Lorem ipsum dolor sit amet, consectetur adipiscing elit, sed do eiusmod tempor incididunt ut labore et dolore magna aliqua. Ut enim ad minim veniam quis nostrud</p>
  <ul class="svc-list" style="left:94px;top:955px;font-size:8.6px">
    <li style="height:25px"><svg class="tick" width="11" height="11" style="margin-right:6px"><use href="#i-tick"/></svg>Water Heater Replacement</li>
    <li style="height:25px"><svg class="tick" width="11" height="11" style="margin-right:6px"><use href="#i-tick"/></svg>Tankless Water Heater Installation</li>
    <li style="height:25px"><svg class="tick" width="11" height="11" style="margin-right:6px"><use href="#i-tick"/></svg>Bath And Kitchen Remodel</li>
    <li style="height:25px"><svg class="tick" width="11" height="11" style="margin-right:6px"><use href="#i-tick"/></svg>Drain Cleaning And Clog Removal</li>
    <li style="height:25px"><svg class="tick" width="11" height="11" style="margin-right:6px"><use href="#i-tick"/></svg>Leak Repair</li>
    <li style="height:25px"><svg class="tick" width="11" height="11" style="margin-right:6px"><use href="#i-tick"/></svg>Faucet Repair And Replacement</li>
  </ul>
  <div class="btn btn--light" style="left:94px;top:1108px;width:88px;height:22px;font-size:7.5px">CONTACT US</div>
  <div class="frame frame--white" style="left:356px;top:944px;width:251px;height:200px"><div class="photo ph-sink" role="img" aria-label="Photo of a plumber in blue overalls working under a sink"></div></div>

  <!-- reviews -->
  <h3 class="sec-title abs" style="left:0;top:1330px;width:702px;text-align:center;font-size:15.5px">CLIENT <em>REVIEWS</em></h3>
  <div class="review" style="left:97px;top:1362px;width:161px;height:136px">
    <i class="g-dot" style="left:12px;top:9px"></i>
    <div class="stars" style="left:12px;top:21px"><svg><use href="#i-star"/></svg><svg><use href="#i-star"/></svg><svg><use href="#i-star"/></svg><svg><use href="#i-star"/></svg><svg><use href="#i-star"/></svg></div>
    <p style="left:12px;top:31px;width:142px;font-size:5.8px;line-height:13px">Lorem Ipsum is simply dummy text of the printing andtting industry. Lorem Ipsum has been the industry's standardy text ever since the 1500s...</p>
    <div class="who" style="left:12px;top:94px;font-size:7px">DANA WHITFIELD</div>
    <div class="stars" style="left:12px;top:104px"><svg><use href="#i-star"/></svg><svg><use href="#i-star"/></svg><svg><use href="#i-star"/></svg><svg><use href="#i-star"/></svg><svg><use href="#i-star"/></svg></div>
    <div class="quote" style="left:122px;top:104px;font-size:34px;line-height:30px">&ldquo;</div>
  </div>
  <div class="review" style="left:271px;top:1362px;width:161px;height:136px">
    <i class="g-dot" style="left:12px;top:9px"></i>
    <div class="stars" style="left:12px;top:21px"><svg><use href="#i-star"/></svg><svg><use href="#i-star"/></svg><svg><use href="#i-star"/></svg><svg><use href="#i-star"/></svg><svg><use href="#i-star"/></svg></div>
    <p style="left:12px;top:31px;width:142px;font-size:5.8px;line-height:13px">Lorem Ipsum is simply dummy text of the printing andtting industry. Lorem Ipsum has been the industry's standardy text ever since the 1500s...</p>
    <div class="who" style="left:12px;top:94px;font-size:7px">ROSA LINDQVIST</div>
    <div class="stars" style="left:12px;top:104px"><svg><use href="#i-star"/></svg><svg><use href="#i-star"/></svg><svg><use href="#i-star"/></svg><svg><use href="#i-star"/></svg><svg><use href="#i-star"/></svg></div>
    <div class="quote" style="left:122px;top:104px;font-size:34px;line-height:30px">&ldquo;</div>
  </div>
  <div class="review" style="left:445px;top:1362px;width:161px;height:136px">
    <i class="g-dot" style="left:12px;top:9px"></i>
    <div class="stars" style="left:12px;top:21px"><svg><use href="#i-star"/></svg><svg><use href="#i-star"/></svg><svg><use href="#i-star"/></svg><svg><use href="#i-star"/></svg><svg><use href="#i-star"/></svg></div>
    <p style="left:12px;top:31px;width:142px;font-size:5.8px;line-height:13px">Lorem Ipsum is simply dummy text of the printing andtting industry. Lorem Ipsum has been the industry's standardy text ever since the 1500s...</p>
    <div class="who" style="left:12px;top:94px;font-size:7px">MARA ELLISON</div>
    <div class="stars" style="left:12px;top:104px"><svg><use href="#i-star"/></svg><svg><use href="#i-star"/></svg><svg><use href="#i-star"/></svg><svg><use href="#i-star"/></svg><svg><use href="#i-star"/></svg></div>
    <div class="quote" style="left:122px;top:104px;font-size:34px;line-height:30px">&ldquo;</div>
  </div>

  <!-- inquiry -->
  <svg class="abs" style="left:0;top:1530px" width="702" height="400" viewBox="0 0 702 400"><polygon points="0,160 347,34 702,134 702,400 0,400" fill="#ececec"/><polygon points="0,138 347,10 702,108 702,134 347,34 0,160" fill="#2d5c9c"/></svg>
  <div class="photo ph-van" style="left:12px;top:1706px;width:340px;height:282px" role="img" aria-label="Illustration of a smiling plumber with tool bags beside a white company van"></div>
  <h3 class="sec-title abs" style="left:379px;top:1680px;font-size:15px">QUICK <em>INQUIRY</em></h3>
  <div class="field" style="left:379px;top:1716px;width:109px;height:22px;font-size:5.6px;padding-left:10px">First Name*</div>
  <div class="field" style="left:497px;top:1716px;width:110px;height:22px;font-size:5.6px;padding-left:10px">Last Name*</div>
  <div class="field" style="left:379px;top:1748px;width:228px;height:22px;font-size:5.6px;padding-left:10px">Your Phone*</div>
  <div class="field" style="left:379px;top:1780px;width:228px;height:22px;font-size:5.6px;padding-left:10px">Your Email*</div>
  <div class="field" style="left:379px;top:1812px;width:228px;height:45px;font-size:5.6px;padding-left:10px;align-items:flex-start;padding-top:8px">Your Message</div>
  <div class="btn" style="left:379px;top:1866px;width:228px;height:22px;font-size:7px">SUBMIT</div>

  <!-- footer -->
  <svg class="abs" style="left:0;top:1900px" width="702" height="342" viewBox="0 0 702 342" role="img" aria-label="Evening city skyline photo under a dark overlay"><polygon points="0,141 347,45 702,130 702,342 0,342" fill="url(#g-city)"/><polygon points="0,100 347,19 702,105 702,130 347,45 0,141" fill="#2d5c9c"/></svg>
  <div class="logo-word" style="left:64px;top:2094px;width:100px;font-size:10.5px;color:#fff">CLEARFLOW<br>PLUMBING</div>
  <div class="foot-h" style="left:237px;top:2055px;font-size:6.8px">CONTACT DETAILS</div>
  <svg class="abs pin" style="left:237px;top:2072px" width="7" height="7"><use href="#i-pin"/></svg>
  <div class="foot-t" style="left:251px;top:2071px;font-size:5.8px;line-height:9px"><b>ADDRESS</b><br>123 Ut Wisi Enim Ad Minim<br>Veniam Quis Nostrud.</div>
  <svg class="abs pin" style="left:237px;top:2109px" width="7" height="7"><use href="#i-phone"/></svg>
  <div class="foot-t" style="left:251px;top:2108px;font-size:5.8px;line-height:9px"><b>PHONE</b><br>123 456 7890</div>
  <svg class="abs" style="left:237px;top:2135px;color:#fff" width="7" height="7"><use href="#i-mail"/></svg>
  <div class="foot-t" style="left:251px;top:2134px;font-size:5.8px;line-height:9px"><b>EMAIL</b><br>info@clearflowplumbing.com</div>
  <div class="foot-h" style="left:400px;top:2055px;font-size:6.8px">QUICK LINKS</div>
  <div class="foot-t" style="left:400px;top:2071px;font-size:6px;line-height:17.5px;font-weight:600;color:#fff">• HOME<br>• ABOUT US<br>• SERVICES<br>• CONTACT US</div>
  <div class="foot-h" style="left:498px;top:2055px;font-size:6.8px">WORKING HOURS</div>
  <div class="hours" style="left:498px;top:2071px;font-size:6px;line-height:17.5px">
    <div><b style="width:30px">MON</b>: 9:00 AM - 9:00PM</div>
    <div><b style="width:30px">TUE</b>: 9:00 AM - 9:00PM</div>
    <div><b style="width:30px">WED</b>: 9:00 AM - 9:00PM</div>
    <div><b style="width:30px">THU</b>: 9:00 AM - 9:00PM</div>
    <div><b style="width:30px">FRI</b>: 9:00 AM - 9:00PM</div>
    <div><b style="width:30px">SAT</b>: 9:00 AM - 9:00PM</div>
  </div>
  <div class="foot-t" style="left:97px;top:2220px;font-size:6px">Copyright © 2023 CLEARFLOW PLUMBING. All Rights Reserved.</div>
  <div class="social" style="left:535px;top:2216px"><i style="width:14px;height:14px"></i><i style="width:14px;height:14px"></i><i style="width:14px;height:14px"></i><i style="width:14px;height:14px"></i></div>
</section>

<!-- ================= mobile page ================= -->
<section class="site" style="left:858px;top:993px;width:221px;height:2516px">
  <div class="topbar">
    <span style="left:12px"><svg class="ico"><use href="#i-phone"/></svg>123-456-7890</span>
    <span style="left:92px"><svg class="ico"><use href="#i-mail"/></svg>info@clearflowplumbing.com</span>
  </div>
  <div class="logo-word" style="left:6px;top:40px;width:90px;font-size:9.5px">CLEARFLOW<br>PLUMBING</div>
  <svg class="abs" style="left:196px;top:51px" width="14" height="10"><rect y="0" width="14" height="1.8" fill="#333"/><rect y="4" width="14" height="1.8" fill="#333"/><rect y="8" width="14" height="1.8" fill="#333"/></svg>
  <div class="photo ph-kitchen" style="left:0;top:88px;width:221px;height:274px" role="img" aria-label="Photo of a plumber greeting a homeowner in a kitchen"></div>
  <div class="hero-box" style="left:14px;top:138px;width:157px;height:130px">
    <div class="hero-serif abs" style="left:8px;top:10px;font-size:12px">CLEARFLOW</div>
    <div class="hero-sans abs" style="left:8px;top:25px;font-size:9.6px">PLUMBING SERVICES</div>
    <p class="hero-copy abs" style="left:8px;top:42px;width:128px;font-size:7.2px;line-height:12.5px">Lorem ipsum dolor sit amet, consectetur adipiscij incididunt ut laboreet dolore magna olighu atnim amet.</p>
    <div class="btn" style="left:8px;top:104px;width:74px;height:18px;font-size:6.8px">GET A QUOTE</div>
  </div>
  <div class="dots" style="left:91px;top:340px"><i></i><i class="on"></i><i></i></div>
  <svg class="abs" style="left:0;top:330px" width="221" height="34" viewBox="0 0 221 34"><polygon points="0,8 110,30 221,0 221,34 0,34" fill="#5db6d2"/><polygon points="0,18 110,34 221,12 221,34 0,34" fill="#fff"/></svg>

  <h3 class="sec-title abs" style="left:0;top:392px;width:221px;text-align:center;font-size:11.5px;line-height:20px">ABOUT<br>CLEARFLOW <em>PLUMBING</em></h3>
  <div class="frame" style="left:9px;top:445px;width:203px;height:168px"><div class="photo ph-plumber" role="img" aria-label="Photo of a plumber fitting a kitchen faucet"></div></div>
  <div class="body-copy abs" style="left:11px;top:626px;width:199px;font-size:7.6px;line-height:14.7px;text-align:justify">
    <p>Lorem Ipsum is simply dummy text of the printing and typesettiustry. Lorem Ipsum has been the industry's standard dummy text ever since the 1500s, when an unknown printer took a galley of type andrambled it to make a type specimenk. Ithas survived not only five centuries.</p>
    <p style="margin-top:4px">remaining essentially unchanged. It was popularised in the 1960s with the release of Typeset sheets containing Lorem Ipsum passages, and more recently with desktop publishing software like Folio Layout including versions of Lorem Ipsum.</p>
  </div>
  <div class="btn" style="left:68px;top:900px;width:86px;height:20px;font-size:6.8px">CONTACT US</div>

  <svg class="abs" style="left:0;top:930px" width="221" height="560" viewBox="0 0 221 560" role="img" aria-label="Suburban house photo under a blue overlay">
    <polygon points="0,34 110,8 221,34 221,60 0,60" fill="#616469"/>
    <polygon points="0,515 110,535 221,515 221,532 110,552 0,532" fill="#616469"/>
    <polygon points="0,40 110,16 221,40 221,520 110,540 0,520" fill="url(#g-house)"/>
  </svg>
  <h3 class="abs" style="left:0;top:990px;width:221px;text-align:center;color:#fff;font-weight:500;font-size:11.5px">OUR SERVICES</h3>
  <p class="abs" style="left:18px;top:1008px;width:185px;text-align:center;color:#e6eef8;font-size:6.8px;line-height:13px">Lorem ipsum dolor sit amet, consectetur adipiscing elit, sed do eiusmod tempor incididunt ut labore et dolore magna aliqua. Ut enim ad minim veniam quis nostrud</p>
  <div class="frame frame--white" style="left:9px;top:1078px;width:203px;height:168px"><div class="photo ph-sink" role="img" aria-label="Photo of a plumber in blue overalls working under a sink"></div></div>
  <ul class="svc-list" style="left:9px;top:1258px;font-size:7.6px">
    <li style="height:22px"><svg class="tick" width="10" height="10" style="margin-right:12px"><use href="#i-tick"/></svg>Water Heater Replacement</li>
    <li style="height:22px"><svg class="tick" width="10" height="10" style="margin-right:12px"><use href="#i-tick"/></svg>Tankless Water Heater Installation</li>
    <li style="height:22px"><svg class="tick" width="10" height="10" style="margin-right:12px"><use href="#i-tick"/></svg>Bath And Kitchen Remodel</li>
    <li style="height:22px"><svg class="tick" width="10" height="10" style="margin-right:12px"><use href="#i-tick"/></svg>Drain Cleaning And Clog Removal</li>
    <li style="height:22px"><svg class="tick" width="10" height="10" style="margin-right:12px"><use href="#i-tick"/></svg>Leak Repair</li>
    <li style="height:22px"><svg class="tick" width="10" height="10" style="margin-right:12px"><use href="#i-tick"/></svg>Faucet Repair And Replacement</li>
  </ul>
  <div class="btn btn--light" style="left:68px;top:1395px;width:86px;height:20px;font-size:6.8px">CONTACT US</div>

  <h3 class="sec-title abs" style="left:0;top:1500px;width:221px;text-align:center;font-size:11.5px">CLIENT <em>REVIEWS</em></h3>
  <div class="review" style="left:13px;top:1530px;width:195px;height:165px">
    <i class="g-dot" style="left:14px;top:14px;width:12px;height:12px"></i>
    <div class="stars" style="left:14px;top:30px"><svg style="width:7px;height:7px"><use href="#i-star"/></svg><svg style="width:7px;height:7px"><use href="#i-star"/></svg><svg style="width:7px;height:7px"><use href="#i-star"/></svg><svg style="width:7px;height:7px"><use href="#i-star"/></svg><svg style="width:7px;height:7px"><use href="#i-star"/></svg></div>
    <p style="left:14px;top:44px;width:170px;font-size:7px;line-height:14.5px">Lorem Ipsum is simply dummy text of the printing andtting industry. Lorem Ipsum has been the industry's standardy text ever since the 1500s...</p>
    <div class="who" style="left:14px;top:118px;font-size:8px">DANA WHITFIELD</div>
    <div class="stars" style="left:14px;top:130px"><svg style="width:7px;height:7px"><use href="#i-star"/></svg><svg style="width:7px;height:7px"><use href="#i-star"/></svg><svg style="width:7px;height:7px"><use href="#i-star"/></svg><svg style="width:7px;height:7px"><use href="#i-star"/></svg><svg style="width:7px;height:7px"><use href="#i-star"/></svg></div>
    <div class="quote" style="left:160px;top:136px;font-size:36px;line-height:30px">&ldquo;</div>
  </div>

  <svg class="abs" style="left:0;top:1718px" width="221" height="46" viewBox="0 0 221 46"><polygon points="0,34 110,4 221,34 221,46 110,18 0,46" fill="#2d5c9c"/></svg>
  <h3 class="sec-title abs" style="left:0;top:1776px;width:221px;text-align:center;font-size:11.5px">QUICK <em>INQUIRY</em></h3>
  <div class="field" style="left:10px;top:1800px;width:97px;height:22px;font-size:6.2px;padding-left:9px">First Name*</div>
  <div class="field" style="left:114px;top:1800px;width:97px;height:22px;font-size:6.2px;padding-left:9px">Last Name*</div>
  <div class="field" style="left:10px;top:1833px;width:201px;height:22px;font-size:6.2px;padding-left:9px">Your Phone*</div>
  <div class="field" style="left:10px;top:1867px;width:201px;height:22px;font-size:6.2px;padding-left:9px">Your Email*</div>
  <div class="field" style="left:10px;top:1901px;width:201px;height:52px;font-size:6.2px;padding-left:9px;align-items:flex-start;padding-top:8px">Your Message</div>
  <div class="btn" style="left:10px;top:1970px;width:201px;height:21px;font-size:7px">SUBMIT</div>

  <svg class="abs" style="left:0;top:2016px" width="221" height="500" viewBox="0 0 221 500" role="img" aria-label="Evening city skyline photo under a dark overlay"><polygon points="0,46 110,14 221,46 221,500 0,500" fill="url(#g-city)"/><polygon points="0,34 110,2 221,34 221,46 110,14 0,46" fill="#2d5c9c"/></svg>
  <div class="logo-word" style="left:0;top:2092px;width:221px;font-size:11px;color:#fff">CLEARFLOW<br>PLUMBING</div>
  <div class="foot-h" style="left:22px;top:2158px;font-size:7px">CONTACT DETAILS</div>
  <svg class="abs pin" style="left:22px;top:2178px" width="8" height="8"><use href="#i-pin"/></svg>
  <div class="foot-t" style="left:42px;top:2177px;font-size:6.2px;line-height:9.5px"><b>ADDRESS</b><br>123 Ut Wisi Enim Ad Minim Veniam<br>Quis Nostrud.</div>
  <svg class="abs pin" style="left:22px;top:2214px" width="8" height="8"><use href="#i-phone"/></svg>
  <div class="foot-t" style="left:42px;top:2213px;font-size:6.2px;line-height:9.5px"><b>PHONE</b><br>123 456 7890</div>
  <svg class="abs" style="left:22px;top:2243px;color:#fff" width="8" height="8"><use href="#i-mail"/></svg>
  <div class="foot-t" style="left:42px;top:2242px;font-size:6.2px;line-height:9.5px"><b>EMAIL</b><br>info@clearflowplumbing.com</div>
  <div class="foot-h" style="left:22px;top:2284px;font-size:7px">WORKING HOURS</div>
  <div class="hours" style="left:22px;top:2302px;font-size:6.4px;line-height:18px">
    <div><b style="width:36px">MON</b>: 9:00 AM - 9:00 PM</div>
    <div><b style="width:36px">TUE</b>: 9:00 AM - 9:00 PM</div>
    <div><b style="width:36px">WED</b>: 9:00 AM - 9:00 PM</div>
    <div><b style="width:36px">THU</b>: 9:00 AM - 9:00 PM</div>
    <div><b style="width:36px">FRI</b>: 9:00 AM - 9:00 PM</div>
    <div><b style="width:36px">SAT</b>: 9:00 AM - 9:00 PM</div>
  </div>
  <div class="social" style="left:22px;top:2430px"><i style="width:17px;height:17px"></i><i style="width:17px;height:17px"></i><i style="width:17px;height:17px"></i><i style="width:17px;height:17px"></i></div>
  <div class="foot-t" style="left:0;top:2478px;width:221px;text-align:center;font-size:6.2px;line-height:10px">Copyright © 2023 CLEARFLOW PLUMBING.<br>All Rights Reserved.</div>
</section>

<!-- ================= bottom wordmark ================= -->
<div class="brand brand--bottom"><span class="brand-mark"></span><span class="brand-name">CLEARFLOW PLUMBING</span></div>
</body>
</html>
```